Header image for law blog

I need a header image for my blog at www.prairiegavelwire.net.

The colors would match the current site. It would say: "Prairie Gavel Wire: Estate Planning and Real Estate in the Prairie State."

I also want to add in smaller type "Law Office of Ned Farrow 555 014 2738 ned@farrowq.com."

The theme maker suggests a header size of 1600 × 230 pixels.

```html
<!DOCTYPE html>
<html lang="en">
<head>
<meta charset="utf-8">
<title>Prairie Gavel Wire – FHLO 90-day seasoning requirement is back for flips</title>
<link rel="stylesheet" href="https://fonts.googleapis.com/css2?family=Bitter:wght@400&family=Source+Sans+3:ital,wght@0,400;0,700;1,400&display=swap">
<style>
:root{
  --page:#ffffff;
  --cream:#f7f5e7;
  --ink:#141412;
  --body:#2e2e2b;
  --accent:#bc360a;
  --brand:#d54a1c;
  --button:#e05d22;
  --button-dark:#b93207;
  --sky-top:#e9e3d6;
  --sky-mid:#d9d1c1;
  --sky-low:#a8a295;
  --field-line:#d4d0ba;
}
*{box-sizing:border-box;margin:0;padding:0}
html,body{width:1200px;height:790px;overflow:hidden;background:var(--page)}
body{font-family:"Source Sans 3","Source Sans Pro",sans-serif;color:var(--body);position:relative}
a{color:var(--accent);text-decoration:none}

.site-header{position:absolute;left:15px;top:0;width:1170px;height:167px;overflow:hidden}
.header-photo{position:absolute;inset:0;background:linear-gradient(180deg,var(--sky-top) 0%,var(--sky-mid) 55%,var(--sky-low) 100%)}
.header-figure{position:absolute;left:22px;top:0;width:150px;height:167px;background:linear-gradient(180deg,rgba(80,70,60,.25),rgba(50,45,40,.45));border-radius:4px 4px 0 0}
.header-text{position:absolute;left:258px;top:16px}
.brand-name{font-family:"Source Sans 3","Source Sans Pro",sans-serif;font-weight:700;font-size:42px;line-height:48px;color:var(--brand);letter-spacing:.5px}
.brand-tagline{font-weight:700;font-size:21px;color:#1d1b18;margin-top:2px;white-space:nowrap}
.brand-rule{width:630px;height:2px;background:var(--brand);margin-top:6px}
.office-label{font-size:15px;color:#1d1b18;margin-top:5px}
.contact-row{display:flex;align-items:center;gap:9px;font-weight:700;font-size:16px;color:var(--brand);margin-top:0}
.contact-row .name{font-size:17px;margin-right:5px}
.contact-row svg{display:block}
.contact-row .email{margin-left:6px}

.site-nav{position:absolute;left:15px;top:167px;width:1170px;height:34px;background:var(--cream);display:flex;align-items:center;padding-left:205px;font-size:11px;color:var(--ink)}
.site-nav a{color:var(--ink);margin-right:26px}
.site-nav .search{position:absolute;right:210px;top:9px}

.entry{position:absolute;left:264px;top:231px;width:445px}
.entry-title{font-family:"Bitter",Georgia,serif;font-weight:400;font-size:36px;line-height:45px;color:var(--ink)}
.entry-meta{display:flex;gap:14px;font-size:10.5px;margin-top:6px}
.entry-content{font-size:12px;line-height:17.8px;margin-top:20px}
.entry-content p+p{margin-top:17px}
.share-title{font-weight:700;font-size:11.5px;color:var(--ink);margin-top:16px}
.share-icons{display:flex;gap:3px;margin-top:4px}
.share-icons i{width:11px;height:11px;background:#c7c9c4;border-radius:2px}
.comment-link{display:flex;align-items:center;gap:4px;font-size:10.5px;margin-top:14px}

.widget{position:absolute;left:762px;width:219px;background:var(--cream);padding:14px 14px}
.widget-title{font-style:italic;font-weight:400;font-size:14.5px;color:#3b3a35;margin-bottom:12px}
.widget ul{list-style:none;font-size:10.5px;line-height:23px}
.appointment{top:231px;height:99px}
.newsletter{top:349px;height:321px;font-size:9.5px;color:var(--ink)}
.newsletter .intro{line-height:12.5px;margin-top:-2px;margin-bottom:14px}
.field label{display:block;margin-bottom:7px}
.field input{display:block;width:190px;height:23px;border:2px solid var(--field-line);background:#fff;margin-bottom:18px}
.required-note{margin-top:-6px}
.subscribe{display:block;width:152px;height:30px;margin:16px 0 0 19px;background:var(--button);border:none;border-bottom:2px solid var(--button-dark);border-radius:2px;color:#fff;font-family:inherit;font-size:10.5px}
.categories{top:689px;height:120px}
.categories li span{color:var(--body)}
</style>
</head>
<body>

<header class="site-header">
  <div class="header-photo" role="img" aria-label="Hazy city skyline behind a businessman stretching his arms wide"></div>
  <div class="header-figure" role="img" aria-label="Businessman in white shirt and tie holding up his jacket"></div>
  <div class="header-text">
    <h1 class="brand-name">PRAIRIE GAVEL WIRE</h1>
    <p class="brand-tagline">Estate Planning and Real Estate in the Prairie State</p>
    <div class="brand-rule"></div>
    <p class="office-label">Law Office of</p>
    <p class="contact-row">
      <span class="name">NED FARROW</span>
      <svg width="14" height="14" viewBox="0 0 14 14" aria-hidden="true"><rect x="3" y="1" width="8" height="12" rx="1.5" fill="#1d1b18"/><rect x="5" y="3" width="4" height="6" fill="#e3ddcf"/></svg>
      <span>555 014 2738</span>
      <svg class="email" width="15" height="11" viewBox="0 0 15 11" aria-hidden="true"><rect x="0.5" y="0.5" width="14" height="10" fill="#1d1b18"/><path d="M1 1l6.5 5L14 1" stroke="#e3ddcf" stroke-width="1.2" fill="none"/></svg>
      <span>ned@farrowq.com</span>
    </p>
  </div>
</header>

<nav class="site-nav">
  <a href="#">About us</a>
  <a href="#">Archives</a>
  <svg class="search" width="17" height="17" viewBox="0 0 17 17" aria-label="Search"><circle cx="7" cy="7" r="5.5" stroke="#141412" stroke-width="2" fill="none"/><path d="M11 11l5 5" stroke="#141412" stroke-width="2.2"/></svg>
</nav>

<article class="entry">
  <h2 class="entry-title">FHLO 90-day seasoning requirement is back for flips</h2>
  <div class="entry-meta">
    <a href="#">◷ March 1, 2015</a>
    <a href="#">▰ Mortgages, Real Estate-Purchases</a>
    <a href="#">● nfarrow</a>
  </div>
  <div class="entry-content">
    <p>Be careful if you are buying a property that the seller is trying to flip. With a flip, the seller buys a distressed or foreclosed property, fixes it up and then quickly resells it. If you are getting an FHLO mortgage to <a href="#">buy a</a> property being flipped, you will not be able to <a href="#">sign a contract</a> to purchase the property until 90 days after the seller has owned the property.</p>
    <p>The 90 day time period is measured from the date the seller acquired the property (closed on the property) to the dale the seller signs a contract with the new FHLO buyer.<br>
    The purpose of this FHLO <a href="#">“seasoning”</a> rule is to prevent sellers from acquiring a property, doing cosmetic repairs and then reselling it at an inflated price. For the past few years, during the depressed real estate market, FHLO waived this rule and allowed the buyer to sign the contract earlier than 90 days, but that changed on January 1, 2015.<br>
    But now, FHLO is back to enforcing the seasoning requirement.<br>
    I have also found that many lenders will require two appraisals to be done if the buyer is buying a flipped property. This will often delay closing because the parties have to wait for the second appraisal.</p>
  </div>
  <p class="share-title">Share and Enjoy:</p>
  <div class="share-icons" aria-label="Share buttons"><i></i><i></i><i></i><i></i><i></i><i></i><i></i><i></i><i></i><i></i><i></i><i></i></div>
  <a class="comment-link" href="#"><svg width="10" height="9" viewBox="0 0 10 9" aria-hidden="true"><path d="M1 1h8v5H4L2 8V6H1z" fill="#bc360a"/></svg>Leave a comment</a>
</article>

<aside>
  <section class="widget appointment">
    <h3 class="widget-title">Set an appointment</h3>
    <ul><li><a href="#">Schedule a phone appointment</a></li><li><a href="#">Schedule an office appointment</a></li></ul>
  </section>

  <section class="widget newsletter">
    <h3 class="widget-title">Sign up for the Newsletter</h3>
    <p class="intro">Give us your email and we will send you the newsletter every month</p>
    <div class="field"><label>Email Address*</label><input type="text"></div>
    <div class="field"><label>First Name</label><input type="text"></div>
    <div class="field"><label>Last Name</label><input type="text"></div>
    <p class="required-note">* = required field</p>
    <button class="subscribe">Subscribe</button>
  </section>

  <section class="widget categories">
    <h3 class="widget-title">Categories</h3>
    <ul>
      <li><a href="#">Bankruptcy</a> <span>(14)</span></li>
      <li><a href="#">Carry-over basis</a> <span>(1)</span></li>
      <li><a href="#">Elder Law</a> <span>(8)</span></li>
    </ul>
  </section>
</aside>

</body>
</html>
```